Menu Edit

Hello. We need a pricing edit on our current menu and new logo swapped (we already have the new logo), as well as colour changes. Also, we require a takeaway menu, in-store menu and footpath a-frame edit as well. I have attached the files bellow.

```html
<!DOCTYPE html>
<html lang="en">
<head>
<meta charset="utf-8">
<title>Tide &amp; Ember Fish Grill – Menu Cards</title>
<link rel="stylesheet" href="https://fonts.googleapis.com/css2?family=Montserrat:wght@300;400;500;600;700&family=Roboto+Slab:wght@700&family=Fira+Sans:wght@600&display=swap">
<style>
  :root {
    --backdrop: #3b3b3b;
    --card: #1d1d1d;
    --red: #e63312;
    --white: #ffffff;
    --ink: #1d1d1d;
    --rule: #7a2a1c;
  }
  * { margin: 0; padding: 0; box-sizing: border-box; }
  html, body { width: 1200px; height: 1200px; overflow: hidden; }
  body {
    background: var(--backdrop);
    font-family: "Montserrat", sans-serif;
    color: var(--white);
    position: relative;
  }
  .card {
    position: absolute;
    top: 198px;
    width: 543px;
    height: 803px;
    background: var(--card);
    box-shadow: 0 6px 18px rgba(0,0,0,.45);
  }
  .card--hours { left: 38px; }
  .card--platters { left: 622px; }

  .centered {
    position: absolute;
    left: 0; right: 0;
    text-align: center;
    transform: translateY(-50%);
    white-space: nowrap;
  }
  .brand {
    top: 168px;
    font-weight: 600;
    font-size: 27px;
    letter-spacing: .5px;
    display: flex;
    justify-content: center;
    align-items: center;
    gap: 10px;
  }
  .brand__dot {
    width: 12px; height: 12px;
    border-radius: 50%;
    background: var(--red);
  }
  .headline {
    font-family: "Roboto Slab", serif;
    font-weight: 700;
    color: var(--red);
  }
  .card--hours .headline { top: 265px; font-size: 44px; }
  .card--platters .headline { top: 267px; font-size: 36px; }

  .hours { font-size: 21px; font-weight: 400; letter-spacing: .5px; }
  .hours b { font-weight: 700; margin-right: 10px; }
  .hours--weekday { top: 309px; }
  .hours--weekend { top: 338px; }

  .rule { position: absolute; left: 43px; right: 44px; height: 1px; background: var(--rule); }
  .rule--bold { height: 3px; background: var(--red); }

  .service { font-size: 24px; font-weight: 400; letter-spacing: .6px; text-transform: uppercase; }
  .byo { top: 487px; font-family: "Fira Sans", sans-serif; font-weight: 600; font-size: 15px; letter-spacing: .3px; }
  .prep-label { top: 529px; font-size: 18px; letter-spacing: .6px; }
  .prep-options { top: 556px; font-size: 16.5px; letter-spacing: .3px; }

  .platter-item { font-size: 19px; font-weight: 600; letter-spacing: .6px; }
  .card--platters .rule { left: 52px; right: 51px; }
  .includes-title { top: 462px; font-size: 16px; font-weight: 700; letter-spacing: .3px; }
  .includes-text {
    position: absolute;
    left: 60px; right: 60px;
    top: 477px;
    text-align: center;
    font-size: 16px;
    font-weight: 300;
    line-height: 23.3px;
    letter-spacing: .3px;
  }

  .phone-band {
    position: absolute;
    left: 0; right: 0;
    top: 624px;
    height: 77px;
    background: var(--white);
    display: flex;
    justify-content: center;
    align-items: center;
    gap: 12px;
    color: var(--ink);
    font-weight: 700;
    font-size: 56px;
    letter-spacing: 2px;
  }
  .phone-band svg { width: 56px; height: 46px; }
  .web-band {
    position: absolute;
    left: 0; right: 0;
    top: 715px;
    height: 40px;
    background: var(--red);
    display: flex;
    justify-content: center;
    align-items: center;
    font-weight: 700;
    font-size: 22px;
    letter-spacing: .5px;
  }
</style>
</head>
<body>

<section class="card card--hours">
  <div class="centered brand">TIDE &amp; EMBER FISH GRILL <span class="brand__dot"></span></div>
  <h1 class="centered headline">Open Every Day</h1>
  <p class="centered hours hours--weekday"><b>Mon – Thurs</b> 5pm to 9pm</p>
  <p class="centered hours hours--weekend"><b>Fri – Sun</b> 12pm to 9pm</p>
  <div class="rule" style="top:365px"></div>
  <p class="centered service" style="top:390px">Casual Dining | Takeaway</p>
  <p class="centered service" style="top:421px">Online Ordering &amp; Delivery</p>
  <p class="centered service" style="top:452px">Fresh Retail</p>
  <p class="centered byo">BYO Welcome! Wine, Beer &amp; Spirits / Soft Drinks Available</p>
  <div class="rule rule--bold" style="top:509px"></div>
  <p class="centered prep-label">Choose your preparation:</p>
  <p class="centered prep-options">PANKO CRUMBED / TEMPURA BATTERED / GRILLED</p>
  <div class="rule rule--bold" style="top:574px"></div>
  <div class="phone-band">
    <svg viewBox="0 0 56 46" aria-hidden="true">
      <path fill="#e63312" d="M4 14 C4 4 52 4 52 14 L52 18 L40 18 L40 12 L16 12 L16 18 L4 18 Z"/>
      <path fill="#e63312" d="M14 20 L42 20 L50 44 L6 44 Z"/>
      <g fill="#fff"><rect x="22" y="27" width="3" height="3"/><rect x="27" y="27" width="3" height="3"/><rect x="32" y="27" width="3" height="3"/><rect x="22" y="32" width="3" height="3"/><rect x="27" y="32" width="3" height="3"/><rect x="32" y="32" width="3" height="3"/></g>
    </svg>
    <span>3555 0142</span>
  </div>
  <div class="web-band">www.tideandember.com.au</div>
</section>

<section class="card card--platters">
  <div class="centered brand">TIDE &amp; EMBER FISH GRILL <span class="brand__dot"></span></div>
  <h1 class="centered headline">Cooked Seafood Platters</h1>
  <p class="centered platter-item" style="top:329px">Cooked Platter for One</p>
  <div class="rule" style="top:348px"></div>
  <p class="centered platter-item" style="top:367px">Cooked Platter for Two</p>
  <div class="rule" style="top:386px"></div>
  <p class="centered platter-item" style="top:406px">Cooked Platter for Three</p>
  <div class="rule" style="top:425px"></div>
  <p class="centered includes-title">Cooked Seafood Platters include:</p>
  <p class="includes-text">Queensland whiting, calamari, salt &amp; pepper calamari, ocean king prawns, sea scallops, beer battered chips, one of our freshly made salads, homemade tartare sauce, lemon &amp; parsley.</p>
  <div class="phone-band">
    <svg viewBox="0 0 56 46" aria-hidden="true">
      <path fill="#e63312" d="M4 14 C4 4 52 4 52 14 L52 18 L40 18 L40 12 L16 12 L16 18 L4 18 Z"/>
      <path fill="#e63312" d="M14 20 L42 20 L50 44 L6 44 Z"/>
      <g fill="#fff"><rect x="22" y="27" width="3" height="3"/><rect x="27" y="27" width="3" height="3"/><rect x="32" y="27" width="3" height="3"/><rect x="22" y="32" width="3" height="3"/><rect x="27" y="32" width="3" height="3"/><rect x="32" y="32" width="3" height="3"/></g>
    </svg>
    <span>3555 0142</span>
  </div>
  <div class="web-band">www.tideandember.com.au</div>
</section>

</body>
</html>
```